Charity donation cards

I need a card in an envelope that would be given out to people and they would put their donations along with their details (name and email) and give it back to us (dropped in acrylic boxes at events etc).

The card should be a medium size, bi or tri fold to be able to fit all the information i require.

The Tovira Fund

The Bright Meadow Centre is dedicated to providing the much needed support to families and children struggling with their differences through a holistic and comprehensive approach that includes detailed evaluations, therapy programs and support services to help unlock the potential in every child.

We are so proud to be able to help empower our society by dedicating our business to the mental, physical and social well being of our younger community and pledging all our net profits to help ensure no child is ever left behind.

Professional services can often be expensive. Our Tovira Fund helps support families requiring financial aid. We believe every child deserves the opportunity to succeed and no child should be left behind.

How can you help?

Gift the therapies to the children that need it the most. We welcome new sponsors, appreciate your gifts and gratefully accept your contributions as we expand to increase the number of children we can serve.

Name:
Email:
Amount:

We accept cash, checks or credit card payments at The Bright Meadow Centre.

Gift cards should be dropped in the designated acrylic boxes at TBMC or the event.

Please email tovirafund@kovelmint.ae for more information on the process.
Http://www.kovelmint.ae

Target Market(s)

These cards will be placed in the reception for our clients to donate.

We will also be working with party planners. Some parents don't want people to get them gifts for their kids birthday party so they want to use this instead.

Industry/Entity Type

Charity

Requirements
Must have
• The same feel as our centre Http://www.kovelmint.ae
• our website, email and contact number
Nice to have
• Go to our website and feel free to take ideas and content.
• The design should be clean and simple.
• High light the key words in the text with bold and maybe in green to make it pop out.
Should not have
• Do not use the word donate in any print material. The word should be gift.

```html
<!DOCTYPE html>
<html lang="en">
<head>
<meta charset="utf-8">
<title>The Tovira Fund – Gift Card</title>
<link rel="stylesheet" href="https://fonts.googleapis.com/css2?family=Open+Sans:wght@400;600;700&display=swap">
<style>
  :root {
    --green-deep: #0b6a3c;
    --green-mid: #137a45;
    --green-bright: #2aa84a;
    --green-mint: #27b56e;
    --ink: #2b2b2b;
    --paper: #ffffff;
    --stage: #e8eeeb;
  }
  * { box-sizing: border-box; margin: 0; padding: 0; }
  html, body { width: 1200px; height: 900px; overflow: hidden; }
  body {
    background: var(--stage);
    font-family: "Open Sans", Arial, sans-serif;
    color: var(--ink);
    position: relative;
  }
  .spread {
    position: absolute;
    display: flex;
    box-shadow: 0 6px 18px rgba(0,0,0,.18);
  }
  .spread--inside { left: 80px; top: 70px; }
  .spread--outside { left: 80px; top: 480px; }
  .panel {
    position: relative;
    width: 340px;
    height: 340px;
    background: var(--paper);
    overflow: hidden;
  }
  .panel + .panel { border-left: 1px solid #dfe6e2; }
  .panel__top-band {
    position: absolute; left: 0; right: 0; top: 0;
    height: 14px; background: var(--green-deep);
  }
  .panel__bottom-band {
    position: absolute; left: 0; right: 0; bottom: 0;
    height: 30px; background: var(--green-deep);
  }
  .panel__bottom-band--stripe::before {
    content: ""; position: absolute; left: 0; right: 0; top: -8px;
    height: 8px; background: var(--green-mint);
  }
  .panel__body { position: absolute; left: 26px; right: 26px; top: 44px; }
  .panel-title {
    font-size: 15px; font-weight: 700; color: var(--green-mid);
    margin-bottom: 10px;
  }
  .panel-copy { font-size: 9.6px; line-height: 1.45; margin-bottom: 9px; }
  .donor-fields { list-style: none; font-size: 10px; font-weight: 700; color: var(--green-mid); margin: 4px 0 14px; line-height: 1.5; }
  .payment-note { font-size: 10px; color: var(--green-bright); text-align: center; line-height: 1.4; margin-bottom: 10px; }
  .drop-note { font-size: 8.6px; font-weight: 600; text-align: center; margin-bottom: 16px; }
  .contact-note { font-size: 7.6px; text-align: center; line-height: 1.5; }

  .panel--back .brand-mark { position: absolute; left: 0; right: 0; top: 120px; }
  .panel--back .contact-note { position: absolute; left: 30px; right: 30px; bottom: 60px; }
  .brand-mark {
    display: flex; align-items: center; justify-content: center; gap: 8px;
    font-size: 17px; font-weight: 400; color: #5d5d5d; line-height: 1.15;
  }
  .brand-mark__dot { width: 16px; height: 16px; border-radius: 50%; background: var(--green-bright); flex: none; }

  .panel--cover { background: var(--green-deep); }
  .photo-grid {
    position: absolute; left: 14px; top: 14px; right: 14px; bottom: 14px;
    display: grid; grid-template-columns: 1fr 1fr; grid-template-rows: 1fr 1fr; gap: 6px;
    background: var(--paper); padding: 6px;
  }
  .photo { width: 100%; height: 100%; }
  .photo--a { background: linear-gradient(135deg, #e9c9b2, #f2e6dc 60%, #e38fa6); }
  .photo--b { background: linear-gradient(135deg, #e8d46a, #d9553e 50%, #4a9bd6); }
  .photo--c { background: linear-gradient(135deg, #c98c5a, #e8b98a 55%, #8a6a4f); }
  .photo--d { background: linear-gradient(135deg, #6b4a35, #d9a27e 55%, #b6b0a4); }
  .cover-badge {
    position: absolute; left: 50%; top: 50%; transform: translate(-50%,-50%);
    width: 104px; height: 104px; border-radius: 50%;
    background: var(--green-bright); border: 4px solid var(--paper);
    display: flex; align-items: center; justify-content: center; text-align: center;
    font-size: 12px; font-weight: 600; color: var(--paper); line-height: 1.2; padding: 10px;
  }

  .envelope {
    position: absolute; left: 830px; top: 300px;
    width: 290px; height: 420px;
    background: var(--green-deep);
    box-shadow: 0 6px 18px rgba(0,0,0,.18);
  }
  .envelope__flap { position: absolute; left: 0; top: 0; width: 290px; height: 110px; }
  .envelope__window {
    position: absolute; left: 0; right: 0; top: 130px; height: 170px;
    background: var(--paper);
    display: flex; align-items: center; justify-content: center;
  }
  .envelope .brand-mark { font-size: 20px; }
</style>
</head>
<body>

  <section class="spread spread--inside" aria-label="Inside spread">
    <article class="panel panel--story">
      <div class="panel__top-band"></div>
      <div class="panel__body">
        <h2 class="panel-title">The Tovira Fund</h2>
        <p class="panel-copy">The Bright Meadow Centre is dedicated to providing the much needed support to families and children struggling with their differences through a holistic and comprehensive approach that includes detailed evaluations, therapy programs and support services to help unlock the potential in every child.</p>
        <p class="panel-copy">We are so proud to be able to help empower our society by dedicating our business to the mental, physical and social well being of our younger community and pledging all our net profits to help ensure no child is ever left behind.</p>
        <p class="panel-copy">Professional services can often be expensive. Our Tovira Fund helps support families requiring financial aid. We believe every child deserves the opportunity to succeed and no child should be left behind.</p>
      </div>
      <div class="panel__bottom-band"></div>
    </article>
    <article class="panel panel--pledge">
      <div class="panel__top-band"></div>
      <div class="panel__body">
        <h2 class="panel-title">How can you help?</h2>
        <p class="panel-copy"><strong>Gift the therapies to the children that need it the most. We welcome new sponsors, appreciate your gifts and gratefully accept your contributions as we expand to increase the number of children we can serve.</strong></p>
        <ul class="donor-fields">
          <li>Name:</li>
          <li>Email:</li>
          <li>Amount:</li>
        </ul>
        <p class="payment-note">We accept cash, cheques or credit card payments<br>at The Bright Meadow Centre.</p>
        <p class="drop-note">Gift cards should be dropped in the designated acrylic boxes at TBMC or the event.</p>
        <p class="contact-note">Please email tovirafund@kovelmint.ae for more information on the process.<br>Http://www.kovelmint.ae</p>
      </div>
      <div class="panel__bottom-band"></div>
    </article>
  </section>

  <section class="spread spread--outside" aria-label="Outside spread">
    <article class="panel panel--back">
      <div class="panel__top-band"></div>
      <div class="brand-mark"><span class="brand-mark__dot"></span><span>The Bright Meadow<br>Centre</span></div>
      <p class="contact-note">Please email tovirafund@kovelmint.ae for more information on the process.<br>Http://www.kovelmint.ae</p>
      <div class="panel__bottom-band panel__bottom-band--stripe"></div>
    </article>
    <article class="panel panel--cover">
      <div class="photo-grid">
        <div class="photo photo--a" role="img" aria-label="Photo of a young girl drawing"></div>
        <div class="photo photo--b" role="img" aria-label="Photo of two boys in a ball pit"></div>
        <div class="photo photo--c" role="img" aria-label="Photo of a boy writing at a desk"></div>
        <div class="photo photo--d" role="img" aria-label="Photo of a smiling girl"></div>
      </div>
      <div class="cover-badge">The Bright Meadow Centre</div>
    </article>
  </section>

  <section class="envelope" aria-label="Envelope">
    <svg class="envelope__flap" viewBox="0 0 290 110" aria-hidden="true">
      <polygon points="0,0 290,0 145,100" fill="#137a45"/>
    </svg>
    <div class="envelope__window">
      <div class="brand-mark"><span class="brand-mark__dot"></span><span>The Bright Meadow<br>Centre</span></div>
    </div>
  </section>

</body>
</html>
```